Commercial refrigeration company requires a one page website. A new wave,fresh looking trade service

Hi,
I have a logo design package already created and I will upload it for your use. All the files are editable and I need the website to match the vibe of my logo and business card designs. It only needs to be a single page as I will not be putting a lot of information on it.
My company services, maintains, sells and installs commercial refrigeration equipment such as: cool rooms, freezer rooms, display fridges, ice makers & beer systems. I don't want it to look like the rest of the companies in my industry. They mostly use ice cubes, mountains, snowmen and other predictable graphics in their pages.
I would like mine to be clean, fresh, easy to understand without those sorts of graphics.
In brief I require a website mostly consisting of the fonts, logos and colours that my graphic designer has created.
I have a quick website made already though its too basic and doesn't stand out. It doesn't use the charcoal colour like the back of my business card which I like, the logo doesn't continue the colours right across the page and is missing a creative spark.
Please refer to www.tandova-cooling.com.au. It has a detailed description of my business for you to use. I need to keep this address so please inform me of how to do this.
I have also included a certification tick I would like somewhere on the page and a photo to add a face to my business.
Thank you in anticipation!
Dale

Target Market(s)

Owners and managers of places such as bars, restaurants, pubs, cafes...
Anywhere with a commercial fridge or ice machine

Coding

Coded - Design and coding required

Number of Pages Required

1 page

Font styles to use
Other font styles liked:
• Century Gothic

Colors
333333
fbfbfb
85cae6

Requirements
Must have
• Used fonts and colours as set out in the logo and business cards designs.
• My phone number emphasised. Easy portal for customer to contact business.
Should not have
• Ice cubes, snowmen, chilli's ect

```html
<!DOCTYPE html>
<html lang="en">
<head>
<meta charset="utf-8">
<title>Tandova Cooling</title>
<link href="https://fonts.googleapis.com/css2?family=Questrial&family=Montserrat:wght@500;600;700&family=Lato:wght@400;700&display=swap" rel="stylesheet">
<style>
:root{
  --charcoal:#333333;
  --ice:#85cae6;
  --bright:#5bc3ee;
  --paper:#fbfbfb;
  --steel:#9b9b9b;
  --rule:#d6d6d6;
}
*{box-sizing:border-box;margin:0;padding:0}
html,body{width:847px;height:1200px;overflow:hidden;background:#fff}
body{position:relative;font-family:'Lato',sans-serif;color:var(--charcoal)}
.abs{position:absolute}

/* header */
.header{left:0;top:0;width:847px;height:82px;background:#fff;border-top:2px solid var(--charcoal)}
.brand{left:114px;top:10px;display:flex;align-items:center;gap:10px}
.brand-square{width:42px;height:42px;background:var(--ice)}
.brand-name{font-family:'Questrial',sans-serif;font-size:15px;letter-spacing:3px;color:var(--charcoal);line-height:1.25}
.tab-phone{left:490px;top:0;width:100px;height:22px;background:var(--charcoal);color:#fff;font-family:'Questrial',sans-serif;font-size:11px;display:flex;align-items:center;justify-content:center;gap:5px;clip-path:polygon(0 0,100% 0,100% 100%,10% 100%)}
.tab-mail{left:590px;top:0;width:143px;height:22px;background:var(--ice);color:#fff;font-size:9px;display:flex;align-items:center;justify-content:center;gap:4px;clip-path:polygon(0 0,100% 0,94% 100%,0 100%)}
.nav{left:340px;top:44px;display:flex;font-family:'Questrial',sans-serif;font-size:10.5px}
.nav a{color:var(--charcoal);text-decoration:none;padding:0 27px;border-right:1px solid var(--rule);line-height:16px}
.nav a.active{font-weight:700;font-family:'Montserrat',sans-serif;font-size:9.5px}

/* hero */
.hero{left:0;top:82px;width:847px;height:344px;background:linear-gradient(180deg,#9fb1be 0%,#7b8791 45%,#5d5f62 70%,#6f6d6a 100%)}
.hero-title{left:116px;top:292px;font-family:'Montserrat',sans-serif;font-weight:700;font-size:16.5px;color:#fff;line-height:22px}
.hero-sub{left:116px;top:336px;font-family:'Montserrat',sans-serif;font-weight:600;font-size:11.5px;color:var(--bright)}

/* sections */
.section-title{width:847px;left:0;text-align:center;font-family:'Montserrat',sans-serif;font-weight:600;font-size:20px}
.section-title span{color:var(--bright)}
.divider{left:272px;width:303px;height:1px}
.welcome-text{left:122px;top:510px;width:604px;text-align:center;font-size:8.2px;line-height:16.9px;color:#222}
.welcome-text p+p{margin-top:4px}

.services{left:0;top:681px;width:847px;height:314px;background:var(--steel)}
.service{width:200px;text-align:center;font-family:'Montserrat',sans-serif;font-weight:600;font-size:12.5px;color:#fff}
.service svg{display:block;margin:0 auto 10px}

/* footer */
.footer{left:0;top:995px;width:847px;height:176px;background:var(--charcoal)}
.badge{left:114px;top:1024px;width:148px;height:54px;border:2px solid #fff;border-radius:4px}
.follow{left:114px;top:1095px;width:134px;text-align:center;color:#fff;font-family:'Montserrat',sans-serif;font-weight:600;font-size:10px}
.socials{left:134px;top:1120px;display:flex;gap:5px}
.socials span{width:20px;height:20px;border:1.4px solid #fff;border-radius:50%}
.vline{top:1018px;width:1px;height:128px;background:#4a4a4a}
.foot-head{color:#fff;font-family:'Montserrat',sans-serif;font-weight:600;font-size:9.5px;display:flex;align-items:center;gap:18px}
.foot-head i{display:block;width:28px;height:1px;background:#777}
.contact{left:348px;top:1044px;color:#e8e8e8;font-size:8.8px;line-height:11px}
.contact li{list-style:none;display:flex;gap:7px;margin-bottom:8.5px}
.contact svg{flex:none;margin-top:1px}
.field{border:1px solid #cfcfcf;border-radius:2px;color:#eee;font-size:7px;padding:3px 5px;height:17px}
.submit{left:568px;top:1125px;width:77px;height:21px;background:var(--ice);color:var(--charcoal);font-family:'Montserrat',sans-serif;font-weight:600;font-size:10.5px;text-align:center;line-height:21px;border-radius:2px}
.copyright{left:0;top:1171px;width:847px;height:29px;background:var(--ice);text-align:center;font-size:9px;line-height:29px;color:#222}
</style>
</head>
<body>

<header class="abs header"></header>
<div class="abs brand">
  <div class="brand-square"></div>
  <div class="brand-name">TANDOVA<br>COOLING</div>
</div>
<div class="abs tab-phone">
  <svg width="11" height="11" viewBox="0 0 12 12"><circle cx="6" cy="6" r="5.3" fill="none" stroke="#fff"/><path d="M4 3.4l1 1.3-.6.7c.4.9 1 1.5 1.9 1.9l.7-.6 1.3 1-.5 1C5.9 8.6 3.5 6.2 3.4 4z" fill="#fff"/></svg>
  0400 517 282
</div>
<div class="abs tab-mail">
  <svg width="10" height="8" viewBox="0 0 10 8"><rect x=".5" y=".5" width="9" height="7" fill="none" stroke="#fff"/><path d="M.5 .5L5 4.5 9.5.5" fill="none" stroke="#fff"/></svg>
  info@tandovacooling.com
</div>
<nav class="abs nav">
  <a class="active">Home</a><a>About Us</a><a>Our Services</a><a>Contact Us</a>
</nav>

<section class="abs hero" role="img" aria-label="Photo of the technician standing beside the branded service ute at the beach"></section>
<div class="abs hero-title">COMMERCIAL REFRIGERATION<br>ICEMAKERS &amp; BEER SYSTEMS</div>
<div class="abs hero-sub">24 Hr Service, Sales &amp; Installations</div>

<h1 class="abs section-title" style="top:458px">Welcome To <span>Tandova Cooling</span></h1>
<div class="abs divider" style="top:495px;background:#ccc"></div>
<div class="abs welcome-text">
  <p>Tandova Cooling is a family run company based in Eastern Sydney, providing services in all types of commercial refrigeration.</p>
  <p>Tandova consists of Dale on the tools and taking your calls, whilst his wife Mara is keeping the books in check. Tandova is dedicated to keeping things simple for their clients – speak to the same people and see the same faces. Tandova Cooling also believes in developing tight relationships with their clients, offering a personalised service.Tandova is completely paperless and uses cloud based trade service software to build a complete profile of your venue and equipment allowing Dale to offer the best advice and solutions for your business. Receive a text message when technician Dale is on his way and your invoice straight to your email at time of service. Tandova can take card, cash or cheque payment on siteWorking alongside a close community of refrigeration contractors, electricians and other trade services, Tandova is in a position to get any job done, no matter how big or small. So whether you're a butcher, baker or cocktail shaker, give Dale a call to see how Tandova can serve your business</p>
</div>

<section class="abs services"></section>
<h2 class="abs section-title" style="top:712px">Our <span>Services</span></h2>
<div class="abs divider" style="top:750px;background:#bbb"></div>

<div class="abs service" style="left:117px;top:772px">
  <svg width="48" height="48" viewBox="0 0 48 48" fill="none" stroke="#fff" stroke-width="2"><path d="M6 8l8 8M4 12l6-6M12 16l22 22 5-1 3 4-4 4-3-3 1-5L14 18"/><path d="M42 4L20 26M22 28l-10 10 3 3 10-10"/></svg>
  24hr Service
</div>
<div class="abs service" style="left:324px;top:772px">
  <svg width="58" height="48" viewBox="0 0 58 48" fill="none" stroke="#fff" stroke-width="2"><circle cx="5" cy="4" r="2.5"/><path d="M7 5l9 4v22h36V9H16M16 31l-4 6h38"/><circle cx="20" cy="42" r="4"/><circle cx="44" cy="42" r="4"/></svg>
  Sales
</div>
<div class="abs service" style="left:530px;top:772px">
  <svg width="48" height="48" viewBox="0 0 48 48" fill="none" stroke="#fff" stroke-width="2"><path d="M4 10l6-6 34 34-6 6zM12 12l3-3M17 17l3-3M22 22l3-3"/><path d="M40 4l4 4L12 40l-8 4 4-8z"/></svg>
  Installations
</div>
<div class="abs service" style="left:117px;top:875px">
  <svg width="32" height="56" viewBox="0 0 32 56" fill="none" stroke="var(--bright)" stroke-width="2"><path d="M8 4a4 4 0 018 0v32a9 9 0 11-8 0z"/><circle cx="12" cy="44" r="5" fill="var(--bright)"/><path d="M22 10h6M22 16h4M22 22h6M22 28h4"/></svg>
  Commercial Refrigeration
</div>
<div class="abs service" style="left:324px;top:875px">
  <svg width="40" height="56" viewBox="0 0 40 56" fill="none" stroke="var(--bright)" stroke-width="2"><path d="M4 4h32l-3 48H7z"/><path d="M6 18h28"/><rect x="12" y="24" width="9" height="9"/><rect x="20" y="34" width="9" height="9"/><rect x="11" y="38" width="8" height="8"/></svg>
  Icemakers
</div>
<div class="abs service" style="left:530px;top:875px">
  <svg width="40" height="56" viewBox="0 0 40 56" fill="none" stroke="var(--bright)" stroke-width="2"><path d="M30 4l4 3-10 16"/><path d="M4 26h18v10H4zM14 26v-4h8v14M22 36v6"/><path d="M24 44c0 3-2 6-3 6s-3-3-3-6l3-3z" fill="var(--bright)"/></svg>
  Beer Systems
</div>

<footer class="abs footer"></footer>
<div class="abs badge" role="img" aria-label="Certification badge"></div>
<div class="abs follow">FOLLOW US ON:</div>
<div class="abs socials"><span></span><span></span><span></span><span></span></div>
<div class="abs vline" style="left:309px"></div>
<div class="abs vline" style="left:523px"></div>

<div class="abs foot-head" style="left:347px;top:1019px">Contact Details<i></i></div>
<ul class="abs contact">
  <li><svg width="9" height="11" viewBox="0 0 9 11"><path d="M4.5 11C1.5 7 0 5.5 0 4a4.5 4.5 0 019 0c0 1.5-1.5 3-4.5 7z" fill="#fff"/><circle cx="4.5" cy="4" r="1.6" fill="#333"/></svg><span>Lorem ipsum dolor sit amet<br>consectetuer diam-012345</span></li>
  <li><svg width="9" height="9" viewBox="0 0 10 10"><path d="M1.5 0l2 2.5-1 1.2c.7 1.6 1.9 2.8 3.4 3.5l1.2-1L10 8.3 8.7 10C4 9.6.4 6 0 1.3z" fill="#fff"/></svg><span>0400 517 282</span></li>
  <li><span>ABN: 41 208 337 519</span></li>
  <li><span>Licence No:418207C</span></li>
  <li><svg width="9" height="7" viewBox="0 0 9 7"><rect width="9" height="7" fill="#fff"/><path d="M0 0l4.5 3.5L9 0" fill="none" stroke="#333" stroke-width=".8"/></svg><span>info@tandovacooling.com</span></li>
</ul>

<div class="abs foot-head" style="left:566px;top:1019px">Quick Inquiry<i></i></div>
<div class="abs field" style="left:568px;top:1046px;width:81px">Name</div>
<div class="abs field" style="left:652px;top:1046px;width:81px">Email</div>
<div class="abs field" style="left:568px;top:1068px;width:165px">Subject</div>
<div class="abs field" style="left:568px;top:1091px;width:165px;height:30px">Message</div>
<div class="abs submit">Submit</div>

<div class="abs copyright">Copyright © 2017 Tandova Cooling &nbsp;|&nbsp; All rights reserved</div>

</body>
</html>
```